Multinational, Mobile Telecommunications Software Solution provider needing a powerful banner for Jo

We need a banner ad design for our company "Corvane Systems"
We provide innovative, customer-centric IT solutions to mobile / cellular telecommunications service providers. We empower service providers with highly customizable solutions that can be seamlessly integrated into the existing business processes, and a variety of turnkey solutions that will help optimize business. We have branches in Asia, Africa, Middle East and Europe and currently employ staff of 23 nationalities. We strive to be the employer of choice. We need to communicate a strong people-centric and diverse culture. Our corporate colour is blue - attached is our logo.

Industry/Entity Type

It Company

```html
<!DOCTYPE html>
<html lang="en">
<head>
<meta charset="utf-8">
<title>Corvane Systems — Banner</title>
<link rel="stylesheet" href="https://fonts.googleapis.com/css2?family=Alegreya:wght@700;800&family=Source+Sans+3:wght@300;400&display=swap">
<style>
  :root {
    --navy: #2e3192;
    --maroon: #8a1f3d;
    --sky: #29a9e0;
    --ink: #000000;
    --green: #0b9446;
    --white: #ffffff;
    --grey: #a7a9ac;
    --mark: #4fb6e8;
  }
  html, body {
    margin: 0;
    padding: 0;
    overflow: hidden;
    background: #ffffff;
  }
  .banner {
    position: relative;
    width: 1200px;
    height: 405px;
    overflow: hidden;
    background: var(--navy);
  }
  .banner__bands {
    position: absolute;
    inset: 0;
    width: 1200px;
    height: 405px;
  }
  .band--maroon { fill: var(--maroon); }
  .band--sky { fill: var(--sky); }
  .band--ink { fill: var(--ink); }
  .band--green { fill: var(--green); }
  .band { stroke: #1a1a1a; stroke-width: 1; }

  .brand {
    position: absolute;
    left: 42px;
    top: 36px;
    display: flex;
    align-items: center;
  }
  .brand__dot {
    width: 104px;
    height: 104px;
    border-radius: 50%;
    background: var(--mark);
    flex: none;
  }
  .brand__text {
    margin-left: 52px;
    margin-top: 20px;
    font-family: "Source Sans 3", sans-serif;
    color: var(--grey);
  }
  .brand__name {
    font-weight: 300;
    font-size: 37px;
    line-height: 1;
    letter-spacing: 0.5px;
    margin: 0;
  }
  .brand__tagline {
    font-weight: 300;
    font-size: 24px;
    line-height: 1;
    margin: 6px 0 0 0;
  }

  .intro {
    position: absolute;
    left: 612px;
    top: 70px;
    margin: 0;
    font-family: "Source Sans 3", sans-serif;
    font-weight: 400;
    font-size: 15.5px;
    line-height: 21.5px;
    color: var(--white);
  }

  .headline {
    position: absolute;
    left: 40px;
    top: 190px;
    margin: 0;
    font-family: "Alegreya", serif;
    color: var(--white);
  }
  .headline__lead {
    display: block;
    font-weight: 800;
    font-size: 66px;
    line-height: 66px;
  }
  .headline__rest {
    display: block;
    margin-left: 20px;
    font-weight: 700;
    font-size: 41px;
    line-height: 58px;
    margin-top: 8px;
    letter-spacing: 0.3px;
  }
</style>
</head>
<body>
  <div class="banner">
    <svg class="banner__bands" viewBox="0 0 1200 405" aria-hidden="true">
      <path class="band band--maroon" d="M820,0 Q720,260 440,405 L1200,405 L1200,0 Z"/>
      <path class="band band--sky" d="M955,0 Q880,270 612,405 L1200,405 L1200,0 Z"/>
      <path class="band band--ink" d="M1150,0 Q1110,290 1000,405 L1200,405 L1200,0 Z"/>
      <path class="band band--green" d="M1088,405 Q1140,350 1200,322 L1200,405 Z"/>
    </svg>

    <div class="brand">
      <div class="brand__dot"></div>
      <div class="brand__text">
        <p class="brand__name">Corvane Systems</p>
        <p class="brand__tagline">innovation beyond borders</p>
      </div>
    </div>

    <p class="intro">
      We empower service providers<br>
      with highly customizable solutions<br>
      that can be seamlessly integrated into the existing business processes,<br>
      and a variety of turnkey solutions that will help optimize business.
    </p>

    <h1 class="headline">
      <span class="headline__lead">innovative</span>
      <span class="headline__rest">customer-centric IT solutions to mobile<br>cellular telecommunications service providers</span>
    </h1>
  </div>
</body>
</html>
```